Website for Ferncliff Servicemen Club

Hi I require a website design in WordPress.

It is for a Ferncliff Club (KMU or Club, Hotel/Restaurant).

It will have a section for the club with blogs and news as well as announcements of upcoming events on the front page.

Another major component of the site will be the Chinese restaurant which will have information about the restaurant as well as the ability to order food online (using a eCommerce module at this stage).

I have included the logos for the shop, as well as some hand drawn images that the Chinese restaurant will want included into their page. This may require a vector to be created that is of the same image (must be EXACTLY the same as the images are highly symbolic).

I am happy to increase the budget to include this vector graphic creation upon request and successful submission.

It would be desired for this to be delivered as coded HTML/CSS or Wordpress, however this is negotiable.

Hi all, thanks for the great submissions,.

Just to clarify. This is a pub (hotel, or ex-services club) that has a restaurant. The restaurant is an important aspect the the site, but not the only focus.

Unfortunately the client has offered very little directly, however the front page will need to be a balance of the Resaurant, bar, and the community sentiment of being a ex-services club, I have added some extra images. These may not suiit the website, but show what an kmu is.

Locals who are looking for a nice place to drink, or good quality food.

Restaurant

```html
<!DOCTYPE html>
<html lang="en">
<head>
<meta charset="utf-8">
<title>Ferncliff Club</title>
<link href="https://fonts.googleapis.com/css2?family=Pathway+Gothic+One&family=Questrial&family=Arimo:ital,wght@1,700&display=swap" rel="stylesheet">
<style>
  :root {
    --club-red: #c1151d;
    --brand-red: #b01119;
    --nav-cream: #f4dfc3;
    --wordmark-white: #ffffff;
    --panel-white: #ffffff;
    --text-grey: #6a6a6a;
    --tagline-grey: #7a7a7a;
    --footer-grey: #474747;
    --footer-text: #a8a8a8;
    --icon-grey: #b9b9b9;
  }
  * { box-sizing: border-box; margin: 0; padding: 0; }
  html, body { width: 1200px; height: 723px; overflow: hidden; }
  body {
    position: relative;
    background: var(--club-red);
    font-family: "Arimo", Arial, sans-serif;
  }
  .decor {
    position: absolute;
    border-radius: 45%;
    background: radial-gradient(ellipse at center, rgba(255,255,255,0.12) 0%, rgba(255,255,255,0.05) 60%, rgba(255,255,255,0) 75%);
  }
  .decor-phoenix { left: 0; top: 30px; width: 230px; height: 360px; }
  .decor-dragon { left: 945px; top: 20px; width: 255px; height: 380px; }

  .site-name {
    position: absolute; left: 229px; top: 22px;
    font-family: "Questrial", sans-serif; font-weight: 400;
    font-size: 26px; line-height: 32px;
    color: var(--wordmark-white);
  }
  .main-nav {
    position: absolute; top: 23px; left: 0; width: 1200px; height: 24px;
    font-family: "Pathway Gothic One", sans-serif; font-size: 18px;
    color: var(--nav-cream);
  }
  .main-nav a { position: absolute; color: inherit; text-decoration: none; }
  .nav-caret {
    display: inline-block; margin-left: 6px; vertical-align: middle;
    border-left: 3px solid transparent; border-right: 3px solid transparent;
    border-top: 4px solid var(--nav-cream);
  }
  .nav-glow {
    position: absolute; left: 527px; top: 36px; width: 80px; height: 50px;
    background: radial-gradient(ellipse at center bottom, rgba(255,255,255,0.75) 0%, rgba(255,255,255,0.2) 40%, rgba(255,255,255,0) 70%);
  }

  .content-panel {
    position: absolute; left: 229px; top: 66px; width: 715px; height: 556px;
    background: var(--panel-white);
  }
  .slider-photo {
    position: absolute; left: 28px; top: 28px; width: 488px; height: 250px;
    background: linear-gradient(180deg, #c9322d 0%, #d63b34 35%, #6e4a35 65%, #b07a4d 100%);
  }
  .slider-caption {
    position: absolute; left: 28px; top: 223px; width: 488px; height: 32px;
    background: rgba(40,40,40,0.72);
    color: #fff; font-family: "Questrial", sans-serif; font-size: 13px;
    padding: 8px 12px;
  }
  .slider-dot { position: absolute; top: 282px; width: 8px; height: 8px; border-radius: 50%; }
  .slider-dot.active { left: 260px; background: var(--brand-red); }
  .slider-dot.idle { left: 275px; background: #a9a9a9; }

  .welcome-title {
    position: absolute; left: 534px; top: 24px; width: 175px;
    font-family: "Questrial", sans-serif; font-weight: 400;
    font-size: 20px; line-height: 23px; color: var(--brand-red);
  }
  .welcome-text {
    position: absolute; left: 538px; width: 150px;
    font-size: 9.4px; line-height: 15px; font-style: italic; font-weight: 700;
    color: var(--text-grey);
  }
  .welcome-text.first { top: 82px; }
  .welcome-text.second { top: 157px; }
  .arrangements-link {
    position: absolute; left: 538px; top: 264px;
    font-size: 9.4px; font-style: italic; font-weight: 700;
    color: var(--brand-red); text-decoration: underline;
  }

  .tagline {
    position: absolute; left: 0; top: 300px; width: 715px; text-align: center;
    font-family: "Questrial", sans-serif; font-weight: 400;
    font-size: 23.5px; line-height: 25px; color: var(--tagline-grey);
  }

  .feature { position: absolute; top: 361px; width: 200px; text-align: center; }
  .feature-1 { left: 29px; }
  .feature-2 { left: 261px; }
  .feature-3 { left: 493px; }
  .feature-icon {
    width: 95px; height: 95px; margin: 0 auto; border-radius: 50%;
    background: var(--brand-red); display: flex; align-items: center; justify-content: center;
  }
  .feature-title {
    margin-top: 10px; font-size: 9.4px; font-style: italic; font-weight: 700;
    color: var(--brand-red);
  }
  .feature-text {
    margin-top: 17px; font-size: 9.4px; line-height: 15px; font-style: italic; font-weight: 700;
    color: var(--text-grey);
  }
  .feature-text .accent { color: var(--brand-red); }

  .site-footer {
    position: absolute; left: 229px; top: 622px; width: 715px; height: 41px;
    background: var(--footer-grey);
  }
  .copyright {
    position: absolute; left: 28px; top: 18px;
    font-family: Arial, sans-serif; font-size: 7.5px; color: var(--footer-text);
  }
  .social-links { position: absolute; left: 600px; top: 16px; display: flex; gap: 13px; align-items: center; }
  .social-square { width: 10px; height: 10px; background: var(--icon-grey); }
</style>
</head>
<body>
  <div class="decor decor-phoenix" role="img" aria-label="Faint phoenix illustration in light red"></div>
  <div class="decor decor-dragon" role="img" aria-label="Faint Chinese dragon illustration in light red"></div>

  <div class="site-name">Ferncliff</div>

  <div class="nav-glow"></div>
  <nav class="main-nav">
    <a href="#" style="left:554px">HOME</a>
    <a href="#" style="left:610px">CLUB<span class="nav-caret"></span></a>
    <a href="#" style="left:669px">NEWS</a>
    <a href="#" style="left:723px">RESTAURANT</a>
    <a href="#" style="left:811px">GALLERY<span class="nav-caret"></span></a>
    <a href="#" style="left:892px">BLOG</a>
  </nav>

  <main class="content-panel">
    <div class="slider-photo" role="img" aria-label="Photo of the restaurant dining room with red booths, wooden tables and guests"></div>
    <div class="slider-caption">Nam risus lectus</div>
    <span class="slider-dot active"></span>
    <span class="slider-dot idle"></span>

    <h1 class="welcome-title">Welcome to our Ferncliff Club</h1>
    <p class="welcome-text first">In commodo pulvinar metus, id tristique massa ultrices at. Nulla auctor turpis ut mi pulvinar eu accumsan risus sagittis.</p>
    <p class="welcome-text second">Mauris nunc ligula, ullamcorper vitae accumsan eu, congue in nulla. Cras hendrerit mi quis nisi semper in sodales nisl faucibus. Sed quis quam eu ante ornare hendrerit.</p>
    <a class="arrangements-link" href="#">See our arrangements</a>

    <h2 class="tagline">We are the beauty salon based in New York City.<br>We give your life a lasting refreshing boost!</h2>

    <section class="feature feature-1">
      <div class="feature-icon">
        <svg width="50" height="50" viewBox="0 0 50 50" aria-hidden="true">
          <circle cx="22" cy="8" r="3" fill="#fff"/>
          <path d="M6 24 A16 14 0 0 1 38 24 Z" fill="#fff"/>
          <rect x="3" y="25" width="38" height="3" rx="1.5" fill="#fff"/>
          <path d="M18 30 L30 30 L34 38 L28 44 L22 38 Z" fill="#fff"/>
        </svg>
      </div>
      <h3 class="feature-title">Meet our team of professionals</h3>
      <p class="feature-text">We have an excelent team of<br>professionals who love what they do!<br><span class="accent">Meet the team</span></p>
    </section>

    <section class="feature feature-2">
      <div class="feature-icon">
        <svg width="56" height="50" viewBox="0 0 56 50" aria-hidden="true">
          <circle cx="36" cy="14" r="9" fill="#fff"/>
          <circle cx="36" cy="14" r="3" fill="#b01119"/>
          <path d="M30 20 L8 40 L12 44 L15 41 L18 44 L22 40 L19 37 L34 23 Z" fill="#fff"/>
          <path d="M36 34 L46 26 L56 34 L53 34 L53 46 L39 46 L39 34 Z" fill="#fff"/>
          <rect x="44" y="38" width="4" height="8" fill="#b01119"/>
        </svg>
      </div>
      <h3 class="feature-title">See the products we sell</h3>
      <p class="feature-text">We use only the best products, and we're<br>proud to have them in store for you!<br><span class="accent">Go see all our products</span></p>
    </section>

    <section class="feature feature-3">
      <div class="feature-icon">
        <svg width="30" height="44" viewBox="0 0 30 44" aria-hidden="true">
          <path d="M15 0 A15 15 0 0 1 30 15 C30 25 20 33 15 44 C10 33 0 25 0 15 A15 15 0 0 1 15 0 Z" fill="#fff"/>
          <circle cx="15" cy="14" r="5" fill="#b01119"/>
        </svg>
      </div>
      <h3 class="feature-title">This is where you can find us</h3>
      <p class="feature-text">Call us: +31 70 5550 123<br>Mail us: <span class="accent">info@ferncliffclub.com</span><br>Harbourstreet 12, 4321 CD</p>
    </section>
  </main>

  <footer class="site-footer">
    <p class="copyright">COPYRIGHT © 2014 FERNCLIFF CLUB</p>
    <div class="social-links">
      <span class="social-square"></span>
      <span class="social-square"></span>
      <svg width="12" height="9" viewBox="0 0 12 9" aria-hidden="true">
        <rect x="0" y="0" width="12" height="9" fill="#b9b9b9"/>
        <path d="M0 0 L6 5 L12 0" fill="none" stroke="#474747" stroke-width="1.2"/>
      </svg>
      <span class="social-square"></span>
    </div>
  </footer>
</body>
</html>
```